New Flyer Design Project

I would like to purchase a customized version of a design you have previously submitted - https://www.brivomart.example/design/58204731

I want this to be something that looks really good.
We use this to explain our service agreements.
our website is www.plorvex.example I want to stick with those colors.

```html
<!DOCTYPE html>
<html lang="en">
<head>
<meta charset="utf-8">
<title>Plorvex Support Plans</title>
<link href="https://fonts.googleapis.com/css2?family=Montserrat:wght@400;500;600;700;800&display=swap" rel="stylesheet">
<style>
  :root {
    --brand-red: #9b2226;
    --brand-red-text: #a3262a;
    --ink: #3d3d3f;
    --ink-soft: #555558;
    --sheet: #f1f1f1;
    --backdrop: #d9d9da;
    --white: #ffffff;
  }
  * { margin: 0; padding: 0; box-sizing: border-box; }
  html, body { width: 1200px; height: 1200px; overflow: hidden; }
  body {
    background: var(--backdrop);
    font-family: "Montserrat", Arial, sans-serif;
    color: var(--ink);
    position: relative;
  }
  .flyer {
    position: absolute;
    left: 186px; top: 20px;
    width: 828px; height: 1160px;
    background: var(--sheet);
    overflow: hidden;
  }
  .brand {
    position: absolute; top: 62px; left: 0; width: 100%;
    text-align: center;
  }
  .brand-name {
    display: inline-flex; align-items: center; gap: 12px;
    font-size: 52px; font-weight: 600; letter-spacing: 2px;
    color: #5b5b5e; line-height: 1;
  }
  .brand-dot {
    width: 18px; height: 18px; border-radius: 50%;
    background: var(--brand-red);
  }
  .brand-tagline {
    margin-top: 10px;
    font-size: 15px; font-weight: 500; color: var(--brand-red-text);
  }
  .title-band {
    position: absolute; top: 164px; left: 0; width: 100%; height: 84px;
    background: var(--brand-red);
    display: flex; align-items: center; justify-content: center;
  }
  .title-band h1 {
    color: var(--white); font-size: 42px; font-weight: 800; letter-spacing: 3px;
  }
  .divider {
    position: absolute; left: 418px; top: 307px; width: 2px; height: 678px;
    background: var(--brand-red);
  }
  .plan { position: absolute; top: 275px; }
  .plan-security { left: 28px; width: 380px; }
  .plan-essentials { left: 440px; width: 372px; }
  .plan-icon { display: block; width: 86px; height: 86px; margin: 0 auto; }
  .plan-security .plan-icon { margin-left: 152px; }
  .plan-essentials .plan-icon { margin-left: 141px; }
  .plan-name {
    margin-top: 20px; text-align: center;
    font-size: 33px; font-weight: 800; letter-spacing: 1px; color: var(--ink);
    line-height: 1;
  }
  .plan-security .plan-name, .plan-security .plan-price { margin-left: -20px; margin-right: 20px; }
  .plan-price {
    margin-top: 6px; text-align: center;
    font-size: 26px; font-weight: 500; color: var(--brand-red-text);
  }
  .features { list-style: none; margin-top: 20px; }
  .features li {
    position: relative; padding-left: 22px;
    font-size: 18.5px; line-height: 20px; color: var(--ink-soft);
    margin-bottom: 8.4px;
  }
  .features li::before {
    content: ""; position: absolute; left: 2px; top: 3px;
    width: 6px; height: 11px;
    border-right: 2.5px solid var(--brand-red); border-bottom: 2.5px solid var(--brand-red);
    transform: rotate(40deg);
  }
  .features li.highlight { color: var(--brand-red-text); font-weight: 600; }
  .pricing-band {
    position: absolute; top: 1076px; left: 0; width: 100%; height: 51px;
    background: var(--brand-red);
    display: flex; align-items: center; justify-content: center;
  }
  .pricing-band p { color: var(--white); font-size: 22px; font-weight: 700; letter-spacing: 2.5px; }
  .contact {
    position: absolute; top: 1139px; left: 0; width: 100%;
    display: flex; justify-content: center; align-items: center; gap: 6px;
    font-size: 11.5px; font-weight: 700; letter-spacing: 1.5px; color: var(--ink);
  }
  .contact svg { width: 12px; height: 12px; }
</style>
</head>
<body>
  <main class="flyer">
    <header class="brand">
      <div class="brand-name"><span>PLORVEX</span><span class="brand-dot"></span></div>
      <p class="brand-tagline">plorvex computing systems</p>
    </header>

    <div class="title-band"><h1>PLORVEX SUPPORT PLANS</h1></div>

    <div class="divider"></div>

    <section class="plan plan-security">
      <svg class="plan-icon" viewBox="0 0 86 86" fill="none" stroke="#9b2226" stroke-width="3" stroke-linejoin="round">
        <path d="M43 6 L76 18 V40 C76 60 62 74 43 82 C24 74 10 60 10 40 V18 Z"/>
        <path d="M43 16 L66 25 V41 C66 55 56 66 43 72 C30 66 20 55 20 41 V25 Z" stroke-width="2"/>
        <circle cx="64" cy="62" r="14" fill="#f1f1f1"/>
        <path d="M64 54 V70 M56 62 H72"/>
      </svg>
      <h2 class="plan-name">SECURITY PLUS</h2>
      <p class="plan-price">$75.00</p>
      <ul class="features">
        <li>Unlimited US bases Remote Help Desk Support</li>
        <li class="highlight">On-Site Support</li>
        <li>Managed Endpoint Detection and Response (EDR) Network monitoring and management</li>
        <li>Managed Antivirus</li>
        <li class="highlight">MFA Multifactor Authentication</li>
        <li class="highlight">Security Awareness Training</li>
        <li class="highlight">Enhanced Spam Filtering</li>
        <li class="highlight">DNS filtering</li>
        <li>Proactive System Monitoring</li>
        <li>Security and Vulnerability patching</li>
        <li>Backup and disaster recovery</li>
        <li>Network Management</li>
        <li>Corvane 365 Administration</li>
        <li>Corvane Nimbus Administration</li>
        <li>Corvane Desk and Corvane</li>
        <li>Server support</li>
        <li>Managed DNS</li>
        <li>Hardware and Software Procurement</li>
        <li>Asset Management</li>
      </ul>
    </section>

    <section class="plan plan-essentials">
      <svg class="plan-icon" viewBox="0 0 86 86" fill="none" stroke="#9b2226" stroke-width="2.5">
        <ellipse cx="43" cy="43" rx="40" ry="16"/>
        <ellipse cx="43" cy="43" rx="40" ry="16" transform="rotate(60 43 43)"/>
        <ellipse cx="43" cy="43" rx="40" ry="16" transform="rotate(-60 43 43)"/>
        <rect x="29" y="29" width="28" height="28" rx="4" fill="#f1f1f1" stroke-width="3"/>
        <rect x="33" y="34" width="20" height="7" rx="1.5"/>
        <rect x="33" y="45" width="20" height="7" rx="1.5"/>
      </svg>
      <h2 class="plan-name">IT ESSENTIALS</h2>
      <p class="plan-price">$55.00 PER PC</p>
      <ul class="features">
        <li>Unlimited US bases Remote Help Desk Support *On-Site Support Available*</li>
        <li>Managed Endpoint Detection and Response (EDR) Network monitoring and management</li>
        <li>Managed Antivirus</li>
        <li>Security and Vulnerability patching</li>
        <li>Backup and disaster recovery</li>
        <li>Network Management</li>
        <li>Corvane 365 Administration</li>
        <li>Corvane 365 Backup</li>
        <li>Corvane Nimbus Administration</li>
        <li>Corvane Desk and Corvane Server support</li>
        <li>Managed DNS</li>
        <li>Hardware and Software Procurement</li>
        <li>Asset Management</li>
      </ul>
    </section>

    <div class="pricing-band"><p>ALL PRICING IS PER MONTH PER PC</p></div>

    <footer class="contact">
      <svg viewBox="0 0 12 12" fill="none" stroke="#3d3d3f" stroke-width="1.2"><path d="M6 11 C3 7.5 2 6 2 4.5 A4 4 0 0 1 10 4.5 C10 6 9 7.5 6 11 Z"/><circle cx="6" cy="4.5" r="1.4"/></svg>
      <span>48 HARLOW COURT #210 BRENMOOR, TEXAS 75990 |</span>
      <svg viewBox="0 0 12 12" fill="none" stroke="#3d3d3f" stroke-width="1"><circle cx="6" cy="6" r="5"/><ellipse cx="6" cy="6" rx="2.2" ry="5"/><path d="M1 6 H11"/></svg>
      <span>WWW.PLORVEX.EXAMPLE |</span>
      <svg viewBox="0 0 12 12" fill="#3d3d3f"><path d="M2.5 1 L4.5 1 L5.3 3.6 L4 4.6 C4.7 6 6 7.3 7.4 8 L8.4 6.7 L11 7.5 L11 9.5 C11 10.3 10.3 11 9.5 11 C5 11 1 7 1 2.5 C1 1.7 1.7 1 2.5 1 Z"/></svg>
      <span>(555) 018-4407</span>
    </footer>
  </main>
</body>
</html>
```